Business Card & Logo Design - Hedge Fund

We need a business card and logo design for a hedge fund. The hedge fund is named Morvane Equity LLC. Morvane Equity was created by finance professors and the strategy is based academic research that looks for patterns in stock prices. The design should look conservative, solid, strong. We favor a classic style - nothing flashy. The logo can relate to the name Morvane Equity, or it could involve a symbol design that connotes "science" . We are open to ideas. We do not want alot of colors - but if any, color - blue is preferred. The font that seems to look best for the name (Morvane Equity) is arial black. We are open to ideas. Most important - we want to see a mock up of an actual business card with the logo concept embedded. The business card should include space for : company name, individual name, position title, cell phone, address. We hope to have this work done by Sept. 8.

Target Market(s)

We will be meeting with and giving the business card to institutions and high net worth individuals.

Industry/Entity Type

Investment Advisory

Contact Information for Business Card

Company name - Morvane Equity LLC
Individual name - Peter Dalby
Title - Portfolio Manager
Cell - (412) 555-0187
Address - 2650 Birchmont Lane, Suite 300, Atlanta GA 30327

Font styles to use
Other font styles liked:
• Arial

Colors
3277b5
0255a3
85acd3
cedeed
fdf9cf
d9d9d9
e6e6e6
f04a50
6b449b

Requirements
Must have
• Must have card details that are sited above.
• We would like a logo related to the name (Morvane Equity) or concept of the fund.
Nice to have
• We want conservative / understated / clean crisp look.
• If any colors - we prefer conservative appearance - blue / gray.
• I have enclosed an example of a card style that looks attractive - please do not exactly copy this card. This is not our company or logo. I feel the layout is attractive - just as an example
Should not have
• Avoid too much color.
• I have selected some preferred colors. Please do not use all of the colors - I have selected a few that might work - but I am not sure. We are open to your ideas so please do not feel the need to use all or any of these.

```html
<!DOCTYPE html>
<html lang="en">
<head>
<meta charset="utf-8">
<title>Morvane Equity LLC — Business Card</title>
<link rel="stylesheet" href="https://fonts.googleapis.com/css2?family=Jost:wght@300;600;700&display=swap">
<style>
  :root {
    --page-bg: #f4f4f4;
    --card-bg: #ececec;
    --blue: #2a5ea6;
    --red: #e0545a;
    --icon-grey: #8a8a8a;
    --band-light: #f4a3d4;
    --band-mid: #e064b0;
    --band-dark: #a8186c;
  }
  html, body {
    margin: 0;
    padding: 0;
    width: 1200px;
    height: 1200px;
    overflow: hidden;
    background: var(--page-bg);
    font-family: "Jost", "Futura", sans-serif;
  }
  .card {
    position: absolute;
    left: 60px;
    top: 279px;
    width: 1080px;
    height: 642px;
    background: var(--card-bg);
    box-shadow: 0 6px 18px rgba(0,0,0,0.18);
    overflow: hidden;
  }
  .person {
    position: absolute;
    right: 52px;
    top: 18px;
    text-align: center;
  }
  .person-name {
    margin: 0;
    font-weight: 600;
    font-size: 90px;
    line-height: 1;
    color: var(--blue);
    letter-spacing: 0.5px;
  }
  .person-title {
    margin: 2px 0 0 0;
    font-weight: 700;
    font-size: 26px;
    letter-spacing: 0.6px;
    color: var(--red);
  }
  .company {
    position: absolute;
    left: 244px;
    width: 590px;
    top: 228px;
    text-align: center;
  }
  .company-name {
    margin: 0;
    font-weight: 700;
    font-size: 70px;
    line-height: 1;
    color: var(--blue);
    letter-spacing: 1px;
    white-space: nowrap;
  }
  .company-suffix {
    display: flex;
    align-items: center;
    gap: 10px;
    margin-top: 8px;
    font-weight: 300;
    font-size: 50px;
    line-height: 1;
    color: var(--red);
  }
  .company-suffix::before,
  .company-suffix::after {
    content: "";
    flex: 1;
    height: 1.5px;
    background: var(--red);
  }
  .contacts {
    position: absolute;
    left: 112px;
    top: 428px;
    margin: 0;
    padding: 0;
    list-style: none;
  }
  .contact {
    display: flex;
    align-items: center;
    gap: 22px;
    color: var(--red);
    font-weight: 700;
    height: 37px;
  }
  .contact svg { width: 32px; height: 32px; flex: none; }
  .contact-phone, .contact-address { font-size: 26px; letter-spacing: 0.4px; }
  .contact-web { font-size: 16px; letter-spacing: 0.3px; height: 30px; }
  .band {
    position: absolute;
    left: 0;
    bottom: 0;
    width: 100%;
    height: 30px;
    background: linear-gradient(90deg, var(--band-light) 0%, var(--band-mid) 60%, var(--band-dark) 100%);
  }
  .band::after {
    content: "";
    position: absolute;
    inset: 0;
    background: linear-gradient(180deg, rgba(255,255,255,0.35), rgba(255,255,255,0) 60%);
  }
</style>
</head>
<body>
  <article class="card">
    <header class="person">
      <h1 class="person-name">Peter Dalby</h1>
      <p class="person-title">PORTFOLIO MANAGER</p>
    </header>

    <section class="company">
      <h2 class="company-name">MORVANE EQUITY</h2>
      <div class="company-suffix">LLC</div>
    </section>

    <ul class="contacts">
      <li class="contact contact-phone">
        <svg viewBox="0 0 32 32" aria-hidden="true">
          <circle cx="16" cy="16" r="13" fill="none" stroke="var(--icon-grey)" stroke-width="1.6"/>
          <path d="M13 9 q-3 7 0 14 l3 -1.5 q-1.5 -5.5 0 -11 z" fill="var(--icon-grey)"/>
        </svg>
        <span>(412) 555-0187</span>
      </li>
      <li class="contact contact-address">
        <svg viewBox="0 0 32 32" aria-hidden="true">
          <rect x="3" y="8" width="26" height="17" fill="none" stroke="var(--icon-grey)" stroke-width="1.6"/>
          <path d="M3 8 L16 18 L29 8 M3 25 L13 16 M29 25 L19 16" fill="none" stroke="var(--icon-grey)" stroke-width="1.4"/>
        </svg>
        <span>2650 BIRCHMONT LANE, SUITE 300, ATLANTA GA 30327</span>
      </li>
      <li class="contact contact-web">
        <svg viewBox="0 0 32 32" aria-hidden="true">
          <circle cx="16" cy="16" r="13" fill="none" stroke="var(--icon-grey)" stroke-width="1.5"/>
          <ellipse cx="16" cy="16" rx="6" ry="13" fill="none" stroke="var(--icon-grey)" stroke-width="1.2"/>
          <path d="M3 16 H29 M5 9.5 H27 M5 22.5 H27" stroke="var(--icon-grey)" stroke-width="1.2"/>
        </svg>
        <span>WWW.MORVANEEQUITY.COM</span>
      </li>
    </ul>

    <div class="band"></div>
  </article>
</body>
</html>
```